依頼詳細
****************************
全国各地で少年詩を創作している詩人たちの応募作品の中から、「子どもにもわかる言葉で書かれた文学性の高い詩作品」を選定し発表しているアンソロジーです。
1984年から年刊「明日童謡選」として20年刊継続してまいりました。2004年より「こどもとひらく童心詩選」と改題し、新たな体制で少年詩のより一層の普及と質的向上をめざしています。

参加費:掲載された場合には予価2,400円(税別)の本を5冊以上ご購入いただきます。(割引あり)(別途送料)*別紙の規約など参照。

選定は任期3年で7名の編集委員により実施されております。
現在の編集委員は
杉浦航一郎(詩人・絵本作家)
くらもと・さよこ(詩人)
島田 薫(小説家・緑陵大学教授)
●●●●(詩人)*未確定なので、一旦この記載
●●●●(詩人)*未確定なので、一旦この記載
岡部里香子(青い窓舎 代表取締役)
森川静江(青い窓舎 編集長)

以上7名です。
編集委員により掲載・不掲載が決定しますが、各編集委員には「5点」を持ち点として、校正刷りの段階で優秀な作品に点数を振り分けてもらい、最優秀作品を決定しております。
最優秀賞に賞金などは出ませんが、粗品を贈呈しております。

なお、学校に協力してもらい、校正刷りの段階にて授業などで活用し、子どもたちの感想を直接もらう取り組みをしております。また実際に詩人を授業に招待する活動もしています。
子どもたちには「好きな作品3つ選んで」とお願いをしてコメントをもらっています。
編集委員、子どもたちの集計結果とコメントは刊行される『こどもとひらく童心詩選』に挟み込まれる「ことのは便り」にて紹介させていただいております。集まった子どもの感想は詩人たちにフィードバックしております。(毎年約400名以上の生徒が参加。)

刊行後は主に公共図書館や学校図書館に納品されます。もちろん全国の書店やBookvaleなどでも購入可能です。
*******************************

主に郵送でご案内をします。
全国各地で詩を書いている人、約2,000人にDMする予定です。
DMの一番トップに、今回のチラシを添えたいと考えております。
同封物として、規定や確認書なども同封します。
が、規約などの細かな部分は読まないので、パッと見ただけで「あ〜、子どもたちを読書対象とした作品の募集をしているんだな。」が理解できると嬉しいです。

他者にない特徴としては、上記にもある《校正刷りの段階で学校と協力して授業でも活用している》ことだと感じています。

作品応募・掲載→編集委員・生徒の感想フィードバック→次年度に質的向上した詩作品の応募・・・このサイクルを目指しています。
生徒にとってもテストの点数に関係がない「詩を味わう時間」という贅沢な時間を経験し、言葉の引き出しを増やしてもらっています。

主に郵送でご案内をします。
全国各地で物語を書いている人、約2,000人にDMする予定です。
同封物として、規定や確認書なども同封します。
が、規約などの細かな部分は読まないですし、パッと見ただけで「あ〜、子どもたちを読書対象とした作品の募集をしているんだな。」が理解できると嬉しいです。

投稿は専用の原稿用紙のみ受け付けとなっているので、弊社に問い合わせ(投稿規定や原稿用紙)をいただけるようにしていただけると幸いです。
記載項目
社名、書名、編集委員、締め切り、問い合わせ先など
サイズ
A4
ページ数
片面
希望イメージ
シンプル 複雑
単色 カラフル
暗い 明るい
日常 高級
遊び心 厳粛
未来的 伝統的
女性的 男性的
希望する色
設定なし
納品ファイル
• イラストレーター形式 (.ai)
• フォトショップ形式 (.psd)
補足説明
*今回より編集委員が変更になっております。
*チラシは昨年のワークリンク採用作品です。
■ 選んだ理由

応募内容などの文字が読みやすいこと。
締め切りの3月末の春を迎える寸前の雰囲気を感じること。
などから選ばせていただきました。

■ 提案者全員のお礼・コメント

この度も素敵なご提案をありがとうございました!
票が全て割れるような事態になるくらい、最終的には好みの段階で選考させていただくような結果となりました。
今後ともよろしくお願いします。

```html
<!DOCTYPE html>
<html lang="ja">
<head>
<meta charset="utf-8">
<title>こどもとひらく童心詩選 作品募集</title>
<link rel="stylesheet" href="https://fonts.googleapis.com/css2?family=Noto+Sans+JP:wght@400;500;700&family=Noto+Serif+JP:wght@400;600;700;900&display=swap">
<style>
  :root {
    --paper: #f7f2e6;
    --ink: #3b3128;
    --ink-soft: #5d5247;
    --accent: #a0652f;
    --accent-light: #c9955f;
    --deadline: #e58d98;
    --label: #7b7358;
    --rule: #c9bda4;
    --band: #ece3cf;
    --white: #ffffff;
  }
  * { margin: 0; padding: 0; box-sizing: border-box; }
  html, body { width: 846px; height: 1200px; overflow: hidden; background: var(--paper); }
  body { font-family: "Noto Serif JP", serif; color: var(--ink); }

  .flyer { position: relative; width: 846px; height: 1200px; overflow: hidden; background: var(--paper); }

  .title { position: absolute; left: 40px; top: 24px; font-weight: 700; letter-spacing: 2px; z-index: 2; }
  .title__lead { font-size: 34px; color: var(--ink); }
  .title__book { font-size: 46px; color: var(--accent); font-weight: 900; }
  .title__main { display: block; margin-top: 8px; font-size: 50px; font-weight: 900; color: var(--ink);
    border-bottom: 3px dotted var(--accent-light); padding-bottom: 4px; width: 250px; }

  .intro { position: absolute; left: 40px; top: 262px; width: 285px; font-size: 12px; line-height: 1.8; color: var(--ink-soft); z-index: 2; }

  .deadline { position: absolute; left: 40px; top: 360px; width: 130px; background: var(--deadline); color: var(--white);
    text-align: center; padding: 8px 6px 10px; font-weight: 700; z-index: 2; }
  .deadline__label { font-size: 19px; letter-spacing: 2px; border-bottom: 1px solid rgba(255,255,255,.7); padding-bottom: 3px; margin-bottom: 5px; }
  .deadline__date { font-size: 17px; line-height: 1.3; }

  .illustration { position: absolute; left: 335px; top: 150px; width: 250px; height: 295px;
    border-radius: 48% 48% 40% 40%;
    background: radial-gradient(ellipse at 50% 45%, #b6875c 0%, #9c6d44 55%, rgba(247,242,230,0) 72%); }

  .message { position: absolute; left: 620px; top: 160px; height: 200px; writing-mode: vertical-rl;
    font-size: 18px; line-height: 1.9; letter-spacing: 3px; color: var(--ink); font-weight: 600; }
  .message__dots { position: absolute; left: 600px; top: 136px; }

  .method { position: absolute; left: 40px; top: 470px; width: 766px; }
  .method__heading { background: var(--band); text-align: center; font-size: 17px; font-weight: 700; letter-spacing: 6px;
    padding: 7px 0; border-top: 1px solid var(--rule); border-bottom: 1px solid var(--rule); }
  .method__table { width: 100%; border-collapse: separate; border-spacing: 0 6px; margin-top: 6px; }
  .method__label { width: 120px; background: var(--label); color: var(--white); font-family: "Noto Sans JP", sans-serif;
    font-size: 14px; font-weight: 500; text-align: center; vertical-align: middle; letter-spacing: 4px; padding: 6px; }
  .method__body { font-family: "Noto Sans JP", sans-serif; font-size: 11.5px; line-height: 1.7; color: var(--ink-soft);
    padding: 6px 10px 6px 16px; border-bottom: 1px dotted var(--rule); }

  .jury { display: grid; grid-template-columns: repeat(3, 1fr); gap: 2px 10px; }
  .jury__name { font-family: "Noto Serif JP", serif; font-size: 14px; font-weight: 600; color: var(--ink); }
  .jury__role { font-size: 10px; color: var(--ink-soft); margin-left: 4px; }

  .contact { position: absolute; left: 0; top: 990px; width: 846px; height: 210px; background: var(--white); }
  .contact__note { position: absolute; left: 40px; top: 18px; width: 766px; text-align: center; font-family: "Noto Sans JP", sans-serif;
    font-size: 13px; color: var(--ink); border-top: 1px solid var(--rule); border-bottom: 1px solid var(--rule); padding: 5px 0; }
  .brand { position: absolute; left: 40px; top: 72px; display: flex; align-items: center; gap: 12px; }
  .brand__mark { width: 54px; height: 54px; border-radius: 50%; background: var(--accent-light); }
  .brand__en { font-family: "Noto Sans JP", sans-serif; font-size: 11px; letter-spacing: 1px; color: var(--ink-soft); }
  .brand__name { font-size: 30px; font-weight: 700; color: var(--ink); letter-spacing: 3px; }
  .address { position: absolute; left: 420px; top: 70px; font-family: "Noto Sans JP", sans-serif; font-size: 12px; color: var(--ink-soft); line-height: 1.7; }
  .phones { display: flex; gap: 26px; font-size: 18px; font-weight: 700; color: var(--ink); }
  .phones svg { vertical-align: -2px; margin-right: 4px; }
</style>
</head>
<body>
<main class="flyer">
  <h1 class="title">
    <span class="title__lead">こどもとひらく</span><span class="title__book">童心詩選</span>
    <span class="title__main">作品募集</span>
  </h1>

  <p class="intro">青い窓舎刊<br>『こどもとひらく童心詩選2019』<br>（アンソロジー詩集）に掲載する作品を募集します。</p>

  <div class="deadline">
    <p class="deadline__label">応募締切</p>
    <p class="deadline__date">2019年<br>3月末日<br>弊社必着</p>
  </div>

  <div class="illustration" role="img" aria-label="本を読む親子の熊のイラスト"></div>

  <svg class="message__dots" width="40" height="30" viewBox="0 0 40 30" aria-hidden="true">
    <circle cx="8" cy="15" r="5" fill="#e58d98"/><circle cx="22" cy="10" r="4" fill="#c9955f"/><circle cx="33" cy="18" r="3" fill="#7b7358"/>
  </svg>
  <p class="message">『言葉』の美しさ、音、色<br>みんなの『言葉』を<br>届けて下さい。</p>

  <section class="method">
    <h2 class="method__heading">応募方法</h2>
    <table class="method__table">
      <tr>
        <th class="method__label">概　要</th>
        <td class="method__body">1984年から年刊「明日童謡選」として20年刊継続し、2004年より「こどもとひらく童心詩選」と改題。全国各地で少年詩を創作している詩人たちの応募作品の中から、「子どもにもわかる言葉で書かれた文学性の高い詩作品」を選定し発表しているアンソロジーです。刊行後は主に公共図書館や学校図書館に納品され、全国の書店やBookvaleなどでも購入可能です。</td>
      </tr>
      <tr>
        <th class="method__label">特　徴</th>
        <td class="method__body">校正刷りの段階で学校に協力していただき、授業で活用して子どもたちの感想を直接いただいています。集まった感想は「ことのは便り」にて紹介し、詩人たちにフィードバックしております。</td>
      </tr>
      <tr>
        <th class="method__label">参加費</th>
        <td class="method__body">掲載された場合には予価2,400円（税別）の本を5冊以上ご購入いただきます。（割引あり）（別途送料）</td>
      </tr>
      <tr>
        <th class="method__label">投稿方法</th>
        <td class="method__body">応募作品は一人一編のみ、投稿規定をご確認の上、規定の原稿用紙にてご応募ください。専用の原稿用紙のみ受け付けとなります。投稿規定や原稿用紙は弊社までお問い合わせください。</td>
      </tr>
      <tr>
        <th class="method__label">選考委員</th>
        <td class="method__body">
          <div class="jury">
            <p><span class="jury__name">杉浦航一郎</span><span class="jury__role">（詩人・絵本作家）</span></p>
            <p><span class="jury__name">●●●●</span><span class="jury__role">（詩人）</span></p>
            <p><span class="jury__name">岡部里香子</span><span class="jury__role">（青い窓舎 代表取締役）</span></p>
            <p><span class="jury__name">くらもと・さよこ</span><span class="jury__role">（詩人）</span></p>
            <p><span class="jury__name">●●●●</span><span class="jury__role">（詩人）</span></p>
            <p><span class="jury__name">森川静江</span><span class="jury__role">（青い窓舎 編集長）</span></p>
            <p><span class="jury__name">島田 薫</span><span class="jury__role">（小説家・緑陵大学教授）</span></p>
          </div>
        </td>
      </tr>
    </table>
  </section>

  <footer class="contact">
    <p class="contact__note">応募先・投稿規定や原稿用紙についてのお問い合わせ</p>
    <div class="brand">
      <span class="brand__mark"></span>
      <div>
        <p class="brand__en">AOIMADO GALLERY &amp; SALON</p>
        <p class="brand__name">青い窓舎</p>
      </div>
    </div>
    <div class="address">
      <p>〒000-0000 架空県青葉市緑町1-2-3</p>
      <div class="phones">
        <p><svg width="16" height="16" viewBox="0 0 24 24" aria-hidden="true"><path fill="#3b3128" d="M6.6 10.8a15.1 15.1 0 0 0 6.6 6.6l2.2-2.2a1 1 0 0 1 1-.25 11.4 11.4 0 0 0 3.6.57 1 1 0 0 1 1 1V20a1 1 0 0 1-1 1A17 17 0 0 1 3 4a1 1 0 0 1 1-1h3.5a1 1 0 0 1 1 1c0 1.25.2 2.45.57 3.57a1 1 0 0 1-.25 1z"/></svg>TEL. 0120-000-111</p>
        <p>FAX. 0120-000-112</p>
      </div>
      <p>e-mail: info@aoimado-sha.example</p>
    </div>
  </footer>
</main>
</body>
</html>
```